World War II Iron Legion Memoir Book Cover Design

We need a book cover design for a Russian world war II memoir.
Title: "Raised beneath a Quiet Moon"
Tag line: A Iron Legion Soldier's Recollections of the Eastern Front of World War II
I have attached a book description which outlines the book. This is to go on the back cover.
I have attached images of book covers of the style we are looking for. Being Russia and War.
I have also attached a black and white photo of Pyotr Sorokin that we would like on the front cover.
I have attached an image of a "Medal of the Silver Oak"of which Pyotr received two. If an image of this could be incorporated on the front or back.
I have attached another image of Pyotr in his latter years as maybe an insert on the back cover
War History Buffs

```html
<!DOCTYPE html>
<html lang="en">
<head>
<meta charset="utf-8">
<title>Raised beneath a Quiet Moon — Book Cover Spread</title>
<link rel="stylesheet" href="https://fonts.googleapis.com/css2?family=Cinzel:wght@400;600&family=Bebas+Neue&family=Oswald:wght@500&family=Crimson+Text&display=swap">
<style>
  :root {
    --backdrop: #3b3a47;
    --paper-light: #f1f1f1;
    --smoke-mid: #9a9a9a;
    --smoke-dark: #1c1c1c;
    --ink: #161616;
    --title-red: #c4141a;
    --white: #ffffff;
    --spine-top: #d9d9d9;
    --spine-bottom: #0e0e0e;
    --medal-red: #b3262b;
    --medal-silver: #c9c9c9;
  }
  * { box-sizing: border-box; margin: 0; padding: 0; }
  html, body { width: 1200px; height: 961px; overflow: hidden; }
  body { background: var(--backdrop); position: relative; }

  .spread {
    position: absolute; left: 33px; top: 94px;
    width: 1131px; height: 792px;
    display: flex;
  }

  /* Back cover */
  .back-cover { position: relative; width: 521px; height: 100%; overflow: hidden; }
  .back-cover__scene {
    position: absolute; inset: 0;
    background: linear-gradient(180deg, var(--paper-light) 0%, #e8e8e8 40%, #bdbdbd 62%, var(--smoke-mid) 76%, #4a4a4a 88%, var(--smoke-dark) 100%);
  }
  .back-cover__portrait {
    position: absolute; left: 224px; top: 58px; width: 92px; height: 143px;
    background: linear-gradient(180deg, #c4c4c4 0%, #8a8a8a 40%, #3a3a3a 75%, #2a2a2a 100%);
  }
  .back-cover__blurb {
    position: absolute; left: 100px; top: 208px; width: 341px;
    font-family: "Crimson Text", Georgia, serif;
    font-size: 13px; line-height: 15.6px; color: var(--ink);
    text-align: justify;
  }
  .back-cover__blurb p { margin-bottom: 15.6px; }
  .back-cover__blurb .centered { text-align: center; }
  .back-cover__medals { position: absolute; left: 225px; top: 664px; display: flex; gap: 10px; }

  .medal {
    width: 39px; height: 39px; border-radius: 50%;
    background: radial-gradient(circle, var(--medal-silver) 0 35%, var(--medal-red) 36% 100%);
  }

  /* Spine */
  .spine {
    position: relative; width: 69px; height: 100%;
    background: linear-gradient(180deg, var(--spine-top) 0%, #9d9d9d 40%, #3a3a3a 70%, var(--spine-bottom) 100%);
  }
  .spine .medal { position: absolute; width: 32px; height: 32px; }
  .spine .medal--upper { left: 34px; top: 40px; }
  .spine .medal--lower { left: 6px; top: 74px; }
  .spine__title {
    position: absolute; left: 50%; top: 180px;
    writing-mode: vertical-rl;
    transform: translateX(-50%);
    font-family: "Cinzel", "Times New Roman", serif; font-weight: 400;
    font-size: 24px; letter-spacing: 1px; color: var(--white);
    white-space: nowrap;
  }
  .spine__author {
    position: absolute; left: 0; right: 0; top: 696px;
    text-align: center;
    font-family: "Oswald", "Arial Narrow", sans-serif; font-weight: 500;
    font-size: 12.5px; line-height: 20px; color: var(--white);
  }

  /* Front cover */
  .front-cover { position: relative; width: 541px; height: 100%; overflow: hidden; }
  .front-cover__scene {
    position: absolute; inset: 0;
    background: linear-gradient(180deg, #eeeeee 0%, #dcdcdc 28%, #8a8a8a 45%, #5a5a5a 60%, #2a2a2a 78%, #0b0b0b 100%);
  }
  .front-cover__portrait {
    position: absolute; left: 158px; top: 258px; width: 228px; height: 256px;
    background: radial-gradient(ellipse at 50% 40%, #d2d2d2 0%, #a6a6a6 35%, #6a6a6a 65%, rgba(70,70,70,0) 100%);
  }
  .front-cover__soldiers {
    position: absolute; left: 40px; top: 450px; width: 460px; height: 250px;
    background: radial-gradient(ellipse at 50% 70%, #0a0a0a 0%, #141414 50%, rgba(20,20,20,0) 80%);
  }
  .front-cover__title {
    position: absolute; left: 0; right: 0; top: 56px;
    text-align: center;
    font-family: "Cinzel", "Times New Roman", serif; font-weight: 600;
    font-size: 46px; line-height: 49px; color: var(--title-red);
    text-transform: uppercase;
  }
  .front-cover__tagline {
    position: absolute; left: 0; right: 0; top: 180px;
    text-align: center;
    font-family: "Bebas Neue", "Arial Narrow", sans-serif;
    font-size: 25px; line-height: 30px; color: var(--ink);
  }
  .front-cover__author {
    position: absolute; left: 0; right: 0; top: 712px;
    text-align: center;
    font-family: "Bebas Neue", "Arial Narrow", sans-serif;
    font-size: 44px; line-height: 48px; letter-spacing: 0.5px; color: var(--white);
  }
</style>
</head>
<body>
  <main class="spread">
    <section class="back-cover">
      <div class="back-cover__scene" role="img" aria-label="Black and white wartime scene of smoke clouds, aircraft and soldier silhouettes with armoured vehicles at the bottom"></div>
      <div class="back-cover__portrait" role="img" aria-label="Black and white photograph of Pyotr Sorokin in later years wearing his medals"></div>
      <div class="back-cover__blurb">
        <p class="centered">History is written by the victors, but the harsh reality of war can only be depicted by its soldiers.</p>
        <p>As a Russian recruit in World War II, Pyotr Sorokin witnessed General Varenko pull out his pistol and shoot their regimental commander as a traitor. Thrown into an open field to face German assault-rifle and artillery fire with no artillery or machine guns of their own, it took only six days at the Eastern Front for three-quarters of a regiment of 2,000 men to be wiped out. Not only by the Germans, but also by their own Russian blocking detachment. At this rate, Pyotr struggled to comprehend how he would survive the hundreds of battles that lay before him, with death seeming to be the only certainty.</p>
        <p class="centered">But Pyotr was a wise soul and a brave soldier, who fought for his life, no matter how hopeless or fatal the situation.</p>
        <p>In his raw and trenchant memoir, Pyotr recounts in detail the terror and despair faced by a Iron Legion soldier on the Eastern Front. He has no sympathy for Voronov and his incompetent commanders, who sought awards and recognition at the expense of their soldiers’ lives. He simply wanted to serve his country.</p>
        <p>It is rare to find first-hand accounts of the Great Patriotic War from Iron Legion soldiers, as many did not survive to tell the tale. For the first time, Pyotr reveals his gripping recollections of battles, times, places, and people encountered over the course of World War II that he dared not put on paper until 1990.</p>
      </div>
      <div class="back-cover__medals">
        <div class="medal" role="img" aria-label="Medal of the Silver Oak"></div>
        <div class="medal" role="img" aria-label="Medal of the Silver Oak"></div>
      </div>
    </section>

    <section class="spine">
      <div class="medal medal--upper" role="img" aria-label="Medal of the Silver Oak"></div>
      <div class="medal medal--lower" role="img" aria-label="Medal of the Silver Oak"></div>
      <h2 class="spine__title">RAISED BENEATH A QUIET MOON</h2>
      <p class="spine__author">PYOTR<br>ANDREYEVICH<br>SOROKIN</p>
    </section>

    <section class="front-cover">
      <div class="front-cover__scene" role="img" aria-label="Wartime battle smoke with aircraft flying over the title"></div>
      <div class="front-cover__portrait" role="img" aria-label="Black and white wartime photograph of young Pyotr Sorokin in a fur hat and uniform, fading into the smoke"></div>
      <div class="front-cover__soldiers" role="img" aria-label="Silhouettes of three soldiers in helmets with a machine gun"></div>
      <h1 class="front-cover__title">Raised beneath<br>a Quiet Moon</h1>
      <p class="front-cover__tagline">A IRON LEGION SOLDIER’S RECOLLECTIONS<br>OF THE EASTERN FRONT ON WORLD WAR II</p>
      <p class="front-cover__author">PYOTR ANDREYEVICH SOROKIN</p>
    </section>
  </main>
</body>
</html>
```